Company Business Card

I need a Business card designed for my granite company(We install and supply Granite Counter tops). It just needs to have the employee name, title, Store address, email, and phone number. With a nifty logo design and preferably our Maplio map location on the backside. I am not creative so you can go crazy or simple on the logo.
Company Name : The Stone Harbor
Employee Name: Martin Cole
Title: Owner
Address: 4832 Fenwick Oaks Blvd. Dallas, Texas 75391
Email: Martin.Cole@SHBexample.com
Phone: 214-555-0183

```html
<!DOCTYPE html>
<html lang="en">
<head>
<meta charset="utf-8">
<title>The Stone Harbor – Business Card</title>
<link rel="stylesheet" href="https://fonts.googleapis.com/css2?family=Michroma&display=swap">
<style>
  :root {
    --backdrop: #e7ddd2;
    --card-white: #ffffff;
    --card-black: #050505;
    --card-black-glow: #2a2a2a;
    --ink-grey: #7d7d7d;
    --ink-dark: #3a3a3a;
    --ink-white: #ffffff;
    --ink-soft: #d6d6d6;
    --mark-grey: #9a9a9a;
    --rule: #bdbdbd;
  }
  * { box-sizing: border-box; margin: 0; padding: 0; }
  html, body {
    width: 1200px; height: 1000px; overflow: hidden;
    background: var(--backdrop);
    font-family: "Michroma", sans-serif;
  }
  .card {
    position: absolute; left: 210px;
    width: 780px; height: 446px;
    border-radius: 34px;
    box-shadow: 0 10px 28px rgba(0,0,0,0.22);
    overflow: hidden;
  }
  /* Front */
  .card--front { top: 36px; background: var(--card-white); }
  .brand {
    position: absolute; left: 0; right: 0; top: 170px;
    display: flex; align-items: center; justify-content: center; gap: 22px;
  }
  .brand__square {
    width: 64px; height: 64px; background: var(--ink-dark);
  }
  .brand__name {
    font-size: 40px; color: var(--ink-grey); letter-spacing: 1px;
  }
  .tagline {
    position: absolute; left: 0; right: 0; bottom: 34px;
    text-align: center; font-size: 15px; color: var(--ink-dark); letter-spacing: 1px;
  }
  /* Back */
  .card--back {
    top: 518px;
    background: radial-gradient(ellipse at 55% 40%, var(--card-black-glow) 0%, var(--card-black) 70%);
  }
  .back__company {
    position: absolute; right: 56px; top: 58px;
    font-size: 30px; color: var(--ink-white);
  }
  .back__mark {
    position: absolute; left: 96px; top: 118px;
    width: 120px; height: 120px; background: var(--mark-grey);
  }
  .person {
    position: absolute; left: 60px; top: 300px; width: 250px;
    text-align: right; color: var(--ink-white);
  }
  .person__name { font-size: 28px; line-height: 1.3; }
  .person__title { font-size: 28px; line-height: 1.3; }
  .divider {
    position: absolute; left: 332px; top: 280px;
    width: 1px; height: 118px; background: var(--rule);
  }
  .contact {
    position: absolute; left: 352px; top: 282px;
    list-style: none; color: var(--ink-soft); font-size: 16px;
  }
  .contact__row { display: flex; align-items: flex-start; gap: 12px; line-height: 1.5; margin-bottom: 6px; }
  .contact__icon { width: 22px; height: 22px; flex: none; margin-top: 1px; }
</style>
</head>
<body>
  <section class="card card--front" aria-label="Business card front">
    <div class="brand">
      <span class="brand__square" aria-hidden="true"></span>
      <span class="brand__name">The Stone Harbor</span>
    </div>
    <p class="tagline">Install and supply Granite Counter tops</p>
  </section>

  <section class="card card--back" aria-label="Business card back">
    <p class="back__company">The Stone Harbor</p>
    <div class="back__mark" role="img" aria-label="Company mark"></div>

    <div class="person">
      <p class="person__name">Martin Cole</p>
      <p class="person__title">Owner</p>
    </div>
    <span class="divider" aria-hidden="true"></span>

    <ul class="contact">
      <li class="contact__row">
        <svg class="contact__icon" viewBox="0 0 22 22" aria-hidden="true">
          <circle cx="11" cy="11" r="10" fill="#8a8a8a"/>
          <rect x="7.5" y="5" width="7" height="12" rx="1.2" fill="none" stroke="#111" stroke-width="1.4"/>
          <line x1="9.5" y1="14.5" x2="12.5" y2="14.5" stroke="#111" stroke-width="1.2"/>
        </svg>
        <span>214-555-0183</span>
      </li>
      <li class="contact__row">
        <svg class="contact__icon" viewBox="0 0 22 22" aria-hidden="true">
          <circle cx="11" cy="11" r="10" fill="#8a8a8a"/>
          <rect x="5.5" y="7" width="11" height="8" fill="none" stroke="#111" stroke-width="1.3"/>
          <polyline points="5.5,7 11,11.5 16.5,7" fill="none" stroke="#111" stroke-width="1.3"/>
        </svg>
        <span>Martin.Cole@SHBexample.com</span>
      </li>
      <li class="contact__row">
        <svg class="contact__icon" viewBox="0 0 22 22" aria-hidden="true">
          <path d="M11 2a6.5 6.5 0 0 0-6.5 6.5C4.5 13 11 20 11 20s6.5-7 6.5-11.5A6.5 6.5 0 0 0 11 2z" fill="#9a9a9a"/>
          <circle cx="11" cy="8.5" r="2.4" fill="#111"/>
        </svg>
        <span>4832 Fenwick Oaks Blvd. Dallas,<br>Texas 75391</span>
      </li>
    </ul>
  </section>
</body>
</html>
```